50 Page Catalog Full Redesign New Look

We are looking for a redesign of our Catalog,

We are looking for a modern redesign of our Catalog, with our new logo most of the products will be the same with some new products as well.
Please use colors in the new logo attached
Attached is our current design please see this for what product will go in the catulog
Updates

Designs look the same

Target Market(s)

Automotive

Font styles to use
Other font styles liked:
• Our Font is outfit

Colors

Designer to choose colors to be used in the design.

```html
<!DOCTYPE html>
<html lang="en">
<head>
<meta charset="utf-8">
<title>Contents – Korvan Promotional</title>
<link rel="stylesheet" href="https://fonts.googleapis.com/css2?family=Outfit:wght@300;400;500;600&display=swap">
<style>
  :root {
    --brand-blue: #0a72b5;
    --ink: #4a4a48;
    --paper: #ffffff;
    --wordmark-blue: #e5eef5;
    --wordmark-grey: #ebebeb;
    --photo-light: #e9f2fa;
    --photo-mid: #7cc3ea;
    --photo-deep: #1f7fc4;
  }
  * { margin: 0; padding: 0; box-sizing: border-box; }
  html, body { width: 848px; height: 1200px; overflow: hidden; }
  body {
    position: relative;
    font-family: "Outfit", sans-serif;
    background: var(--photo-light);
  }
  .backdrop-photo {
    position: absolute; inset: 0;
    background:
      linear-gradient(180deg, var(--photo-light) 0%, #eef5fb 38%, var(--photo-mid) 60%, var(--photo-deep) 80%, #36b5e0 100%);
  }
  .page {
    position: absolute; left: 89px; top: 0; width: 759px; height: 1173px;
    background: var(--paper);
    border-bottom-left-radius: 31px;
  }
  .decor { position: absolute; left: -89px; top: 0; }
  .brand-badge {
    position: absolute; left: -13px; top: 86px; width: 166px; height: 166px;
    border: 3px solid var(--brand-blue); border-radius: 50%;
    background: var(--paper);
    display: flex; align-items: center; justify-content: center;
    color: var(--brand-blue); font-weight: 600; font-size: 27px;
  }
  .page-title {
    position: absolute; left: 183px; top: 160px;
    font-size: 57px; font-weight: 600; color: var(--brand-blue);
    letter-spacing: -0.5px; line-height: 1;
  }
  .toc { position: absolute; left: 0; top: 282px; list-style: none; }
  .toc-item {
    display: flex; align-items: baseline; height: 52.9px;
    font-size: 22px; font-weight: 300; color: var(--ink); line-height: 1;
  }
  .toc-pages { width: 143px; text-align: right; }
  .toc-dots { width: 42px; text-align: center; }
  .toc-title { white-space: nowrap; }
</style>
</head>
<body>
  <div class="backdrop-photo" role="img" aria-label="Soft blue background photograph of car parts and surfaces"></div>

  <div class="page">
    <svg class="decor" width="848" height="1200" viewBox="0 0 848 1200" aria-hidden="true">
      <text transform="translate(718,1050) rotate(-90)" textLength="901" lengthAdjust="spacingAndGlyphs"
            font-family="Outfit, sans-serif" font-weight="500" font-size="205" fill="var(--wordmark-blue)">KORVAN</text>
      <rect x="784" y="149" width="9" height="96" fill="var(--wordmark-grey)"/>
      <rect x="784" y="954" width="9" height="96" fill="var(--wordmark-grey)"/>
      <text transform="translate(820,920) rotate(-90)" textLength="640" lengthAdjust="spacingAndGlyphs"
            font-family="Outfit, sans-serif" font-weight="500" font-size="86" fill="var(--wordmark-grey)">PROMOTIONAL</text>
    </svg>
    <div class="brand-badge">Korvan</div>
    <h1 class="page-title">Contents</h1>
    <ol class="toc">
      <li class="toc-item"><span class="toc-pages">4-5</span><span class="toc-dots">…</span><span class="toc-title">About Us &amp; Our Solutions</span></li>
      <li class="toc-item"><span class="toc-pages">6-7</span><span class="toc-dots">…</span><span class="toc-title">Number Plate Frames</span></li>
      <li class="toc-item"><span class="toc-pages">8-11</span><span class="toc-dots">…</span><span class="toc-title">Keyrings</span></li>
      <li class="toc-item"><span class="toc-pages">12-13</span><span class="toc-dots">…</span><span class="toc-title">Stickers, Mudflaps &amp; Service Book Wallets</span></li>
      <li class="toc-item"><span class="toc-pages">14-15</span><span class="toc-dots">…</span><span class="toc-title">Hand Over Gifts &amp; Caps</span></li>
      <li class="toc-item"><span class="toc-pages">16-19</span><span class="toc-dots">…</span><span class="toc-title">Bottled Water, Stubby Coolers &amp; Car Accessories</span></li>
      <li class="toc-item"><span class="toc-pages">20-21</span><span class="toc-dots">…</span><span class="toc-title">Cooler Bags</span></li>
      <li class="toc-item"><span class="toc-pages">22-23</span><span class="toc-dots">…</span><span class="toc-title">Pens</span></li>
      <li class="toc-item"><span class="toc-pages">24-25</span><span class="toc-dots">…</span><span class="toc-title">Notebooks &amp; Confectionery</span></li>
      <li class="toc-item"><span class="toc-pages">26-27</span><span class="toc-dots">…</span><span class="toc-title">Drinkware &amp; Umbrellas</span></li>
      <li class="toc-item"><span class="toc-pages">28-29</span><span class="toc-dots">…</span><span class="toc-title">Microfibre Cloths &amp; Golf</span></li>
      <li class="toc-item"><span class="toc-pages">30-33</span><span class="toc-dots">…</span><span class="toc-title">Signage &amp; Printed Sanitiser</span></li>
      <li class="toc-item"><span class="toc-pages">34-49</span><span class="toc-dots">…</span><span class="toc-title">Product Ideas</span></li>
      <li class="toc-item"><span class="toc-pages">50</span><span class="toc-dots">…</span><span class="toc-title">Cleaning &amp; Sanitiser</span></li>
      <li class="toc-item"><span class="toc-pages">51</span><span class="toc-dots">…</span><span class="toc-title">Stock Control</span></li>
    </ol>
  </div>
</body>
</html>
```